Pelorn.com- International Goal Achievement Coach Needs Website Design

I need a web design for my new company called Pelorn. I help people who are stuck, people who have a big dream, but don't know how to get there. I help them to break their dreams down into small, manageable steps... and then I'm the "kick in the shin" to get them moving and thriving!

We can all be better- We can all DO better. I inspire people to Go Boldly in the direction of your dreams.

I have uploaded my logo along with some vintage champagne posters. Please use the vintage posters as inspiration. I like the bold, vintage look and feel. I would love the main colors of the design to be black, white and metallic gold. And to follow along this vintage look and feel. Please feel free to use the logo in black or metallic gold or white.

Target Market(s)

websites that I like- lucindavarek.com & tessaw.tv

I would like to also use the vintage champagne photos attached as inspiration as well.

Industry/Entity Type

It Company

Requirements
Must have
• Tabs should include: About, Work With Me, Praise, Giving Back

On the homepage add:
* Sign up for newsletter with space to enter name and email (No click throughs)
* Upcoming Events/Sessions
* Newsletter Posts
* Resources
* Praise Section

* Large photo on top with additional photos throughout the page/site.
Nice to have
• Any additions you can bring to the table would be greatly appreciated.

```html
<!DOCTYPE html>
<html lang="en">
<head>
<meta charset="utf-8">
<title>Pelorn – Go Boldly</title>
<link href="https://fonts.googleapis.com/css2?family=Raleway:ital,wght@0,400;0,500;0,600;0,700;0,800;1,400;1,600&family=Righteous&family=Yesteryear&display=swap" rel="stylesheet">
<style>
:root{
  --gold:#e6ad12;
  --gold-deep:#c8900a;
  --ink:#141414;
  --black:#0d0d0d;
  --paper:#f2f0eb;
  --card:#ffffff;
  --text:#5a5a5a;
  --muted:#9a9a9a;
  --line:#dcd9d2;
  --teal:#22c3d6;
}
*{box-sizing:border-box;margin:0;padding:0}
html,body{width:1200px;height:2314px;overflow:hidden}
body{position:relative;background:var(--paper);font-family:"Raleway",sans-serif;color:var(--text)}
.abs{position:absolute}
.brand{display:flex;align-items:center;gap:8px;font-family:"Raleway",sans-serif;font-weight:700;color:var(--gold)}
.brand .dot{border-radius:50%;background:var(--gold)}

/* header */
.site-header{left:0;top:0;width:1200px;height:55px;background:var(--black)}
.site-header .brand{position:absolute;left:172px;top:10px;font-size:20px}
.site-header .brand .dot{width:34px;height:34px}
.main-nav{position:absolute;top:0;left:559px;height:55px;display:flex;align-items:center;font-size:12.5px;font-weight:600;color:var(--gold);text-transform:uppercase}
.main-nav span{position:absolute;white-space:nowrap}
.gold-rule{left:0;top:55px;width:1200px;height:4px;background:var(--gold)}

/* hero */
.hero{left:0;top:59px;width:1200px;height:397px;background:linear-gradient(90deg,#b7a683 0%,#9aa79d 30%,#c8b58c 60%,#d7bf8e 80%,#b99e6e 100%)}
.hero-photo{left:0;top:59px;width:1200px;height:397px;background:radial-gradient(ellipse 280px 360px at 880px 260px,rgba(232,210,170,.9),rgba(232,210,170,0) 70%),linear-gradient(180deg,rgba(140,170,175,.35),rgba(214,190,140,.4))}
.hero-tagline{left:177px;top:108px;font-family:"Yesteryear",cursive;font-size:42px;color:var(--ink)}
.hero-title{left:174px;top:160px;font-family:"Righteous",sans-serif;font-size:78px;line-height:80px;color:var(--paper);-webkit-text-stroke:2px var(--ink);text-shadow:5px 4px 0 var(--ink);letter-spacing:1px}
.hero-rule{left:177px;top:335px;width:459px;height:3px;background:var(--ink)}
.hero-signup{left:176px;top:347px;font-size:14px;font-weight:800;color:var(--ink);text-transform:uppercase}
.hero-signup small{font-size:11px;font-weight:600;text-transform:none}
.hero-free{left:176px;top:366px;font-size:17px;font-weight:800;color:var(--ink)}
.field{position:absolute;background:#f4f1ea;border:1px solid #d8d2c4;font-size:12.5px;color:#666;padding-left:12px;display:flex;align-items:center}
.btn-sub{position:absolute;background:linear-gradient(#2a2a2a,#050505);color:#fff;font-size:10px;font-weight:700;display:flex;align-items:center;justify-content:center;border-radius:2px}

/* content */
.section-title{left:172px;top:496px;font-size:30px;font-weight:700;color:var(--gold)}
.body-copy{font-size:12.3px;line-height:17.9px;color:var(--text)}
.intro{left:172px;top:540px;width:597px}
.hr{height:1px;background:var(--line)}
.related-head{left:172px;top:765px;font-size:11.5px;font-weight:700;color:var(--ink);text-transform:uppercase}
.thumb{position:absolute;top:790px;width:197px;height:114px}
.thumb-cap{position:absolute;top:909px;width:197px;font-size:12.3px;line-height:18px;color:var(--ink)}
.thumb-cap.active{color:var(--gold);font-weight:600}
.thumb-cap .more{display:block;color:#444;font-size:10.5px;text-decoration:underline;font-weight:500}
.icon-btn{position:absolute;width:27px;height:27px;background:#ececec;border:1px solid #d4d4d4;display:flex;align-items:center;justify-content:center}
.badge{position:absolute;width:16px;height:16px;border-radius:50%;background:var(--teal);color:#fff;font-size:9px;font-weight:700;display:flex;align-items:center;justify-content:center}
.read-more{position:absolute;font-size:12px;color:var(--ink)}

.post{position:absolute;left:172px;width:597px;height:486px;background:var(--card);border:1px solid var(--line)}
.post-img{position:absolute;left:0;top:0;width:595px;height:266px;background:linear-gradient(100deg,#d4c9a8 0%,#c86c56 40%,#e3bf8e 60%,#b9a37e 100%);border:1px solid #7c1a1a}
.post-band{position:absolute;left:0;top:195px;width:595px;height:71px;background:rgba(40,36,28,.82);display:flex;align-items:center;justify-content:space-between;padding:0 22px 0 18px}
.post-band h2{font-size:25px;font-weight:600;color:var(--gold)}
.post-band .brand{font-size:18px}
.post-band .brand .dot{width:32px;height:32px}
.post-meta{position:absolute;left:18px;top:278px;font-size:9.5px;font-style:italic;color:#666}
.post-meta b{font-weight:600;color:var(--ink)}
.post-text{position:absolute;left:18px;top:296px;width:560px}

.load-more{left:301px;top:2061px;width:339px;height:43px;background:#fff;border:1px solid var(--line);display:flex;align-items:center;justify-content:center;gap:10px;font-size:12px;font-weight:800;letter-spacing:2px;color:var(--ink)}

/* sidebar */
.side-label{font-size:13px;font-weight:700;color:var(--ink);text-transform:uppercase}
.social-label{left:788px;top:501px;font-size:12px;font-weight:700;color:var(--gold);line-height:14px}
.soc{position:absolute;top:499px;width:29px;height:29px;border-radius:4px}
.ad{position:absolute;left:788px;width:240px}
.ad1{top:549px;height:134px;background:linear-gradient(90deg,#f3f2f5,#e6e2ea 60%,#d9d1d8)}
.ad1 p{position:absolute;left:12px;top:10px;width:125px;font-size:11.5px;line-height:17px;color:#555}
.ad1 .brand{position:absolute;left:12px;top:100px;font-size:13px}
.ad1 .brand .dot{width:22px;height:22px}
.ad2{top:694px;height:273px;background:linear-gradient(180deg,#f2d9a3,#d79a4e 60%,#8a5a22)}
.ad2 .band{position:absolute;left:0;bottom:0;width:240px;height:78px;background:rgba(170,120,20,.85);padding:10px 12px}
.ad2 .band p{font-size:15px;font-weight:600;line-height:18px;color:#fff;text-transform:uppercase;width:160px}
.ad2 .brand{position:absolute;right:10px;bottom:20px;font-size:15px;color:#fff}
.ad-corner{position:absolute;left:10px;top:10px;width:34px;height:34px;border-radius:50%;background:var(--gold)}
.ad3{top:979px;height:198px;background:linear-gradient(90deg,#2a1d06,#6b4d10 55%,#3a2a08)}
.ad3 p{position:absolute;left:18px;top:70px;font-size:15px;font-weight:700;line-height:18px;color:var(--gold);text-transform:uppercase}
.pop-item{position:absolute;left:788px;width:240px;height:84px}
.pop-img{position:absolute;left:0;top:0;width:84px;height:84px}
.pop-title{position:absolute;left:98px;top:0;width:142px;font-size:10px;font-weight:600;line-height:16px;color:var(--ink);text-transform:uppercase}
.pop-date{position:absolute;left:98px;font-size:9.5px;color:var(--muted)}
.video{left:788px;top:1655px;width:240px;height:127px;background:linear-gradient(135deg,#f1c21b,#d08a08 70%,#a06a05)}
.comment{position:absolute;left:790px;width:238px;height:24px;border-bottom:1px solid #e2dfd8;display:flex;align-items:flex-start;gap:6px;font-size:10px;color:var(--muted)}

/* footer */
.site-footer{left:0;top:2116px;width:1200px;height:198px;background:var(--black)}
.foot-nav span{position:absolute;top:2141px;font-size:12px;font-weight:500;color:#d8d8d8;text-transform:uppercase;white-space:nowrap}
.foot-nav .current{color:var(--gold)}
.site-footer .brand{position:absolute}
.foot-label{font-size:12.5px;font-weight:500;color:#cfcfcf;text-transform:uppercase}
.foot-field{background:#fff;border:none;color:#555}
.foot-soc{position:absolute;top:2232px;width:27px;height:27px;border-radius:3px;background:#555}
</style>
</head>
<body>

<header class="abs site-header">
  <div class="brand"><span class="dot"></span>Pelorn</div>
  <nav class="main-nav">
    <span style="left:0;top:20px">About</span>
    <span style="left:92px;top:20px">Work With Me</span>
    <span style="left:234px;top:20px">Praise</span>
    <span style="left:329px;top:20px">Giving Back</span>
    <svg style="position:absolute;left:437px;top:19px" width="16" height="16" viewBox="0 0 16 16"><circle cx="6.5" cy="6.5" r="5" fill="none" stroke="#e6ad12" stroke-width="1.8"/><line x1="10.2" y1="10.2" x2="14.5" y2="14.5" stroke="#e6ad12" stroke-width="1.8"/></svg>
  </nav>
</header>
<div class="abs gold-rule"></div>

<section class="hero-block">
  <div class="abs hero"></div>
  <div class="abs hero-photo" role="img" aria-label="Vintage-toned photo of a smiling woman sitting on a sunny beach by the sea"></div>
  <div class="abs hero-tagline">We can all be better.</div>
  <h1 class="abs hero-title">WE CAN ALL<br>DO BETTER.</h1>
  <div class="abs hero-rule"></div>
  <p class="abs hero-signup">Sign up for Pelorn Newsletter <small>and Go Boldly In The Direction Of Their Dreams...</small></p>
  <p class="abs hero-free">IT'S FREE</p>
  <div class="field" style="left:175px;top:398px;width:182px;height:30px">First name</div>
  <div class="field" style="left:362px;top:398px;width:182px;height:30px">Email</div>
  <div class="btn-sub" style="left:550px;top:398px;width:88px;height:30px">SUBSCRIBE</div>
</section>

<main>
  <h2 class="abs section-title">THE No.1 KEY TO SUCCESS</h2>
  <p class="abs body-copy intro">Suspendisse blandit ligula turpis, ac convallis risus fermentum non. Duis vestibulum quis quam vel accumsan. Nunc a vulputate lectus. Vestibulum eleifend nisl sed massa sagittis vestibulum. Vestibulum pretium blandit tellus, sodales volutpat sapien varius vel. Phasellus tristique cursus erat, a placerat tellus laoreet eget. Fusce vitae dui sit amet lacus rutrum convallis. Vivamus sit amet lectus venenatis est rhoncus interdum a vitae velit.<br>Suspendisse blandit ligula turpis, ac convallis risus fermentum non. Duis vestibulum quis quam vel accumsan. Nunc a vulputate lectus. Vestibulum eleifend nisl sed massa sagittis vestibulum. Vestibulum pretium blandit tellus, sodales volutpat sapien varius vel. Phasellus tristique cursus erat, a placerat tellus laoreet eget. Fusce vitae dui sit amet lacus rutrum convallis. Vivamus sit amet lectus venenatis est rhoncus interdum a vitae velit.</p>
  <div class="abs hr" style="left:172px;top:741px;width:597px"></div>
  <h3 class="abs related-head">In addition to practicing the #1 key to success, you may also like these posts:</h3>

  <div class="thumb" style="left:172px;background:linear-gradient(180deg,#cfd8dc,#9a8d74)" role="img" aria-label="Photo of a woman reading in a chair on a mountain slope"></div>
  <div class="thumb" style="left:372px;background:linear-gradient(180deg,#b8c23a,#7f9a1e)" role="img" aria-label="Photo of a smiling woman lying in green grass"></div>
  <div class="thumb" style="left:572px;background:linear-gradient(90deg,#f1f1f1,#c9a58c 60%,#eeeeee)" role="img" aria-label="Portrait photo of a smiling woman on a white background"></div>
  <p class="thumb-cap" style="left:172px">The #1 Key to Manifesting</p>
  <p class="thumb-cap active" style="left:372px">How to handle success.<span class="more">View Post</span></p>
  <p class="thumb-cap" style="left:572px">Reclaim your power when you feel powerless.</p>

  <div class="icon-btn" style="left:172px;top:987px"><svg width="13" height="11" viewBox="0 0 13 11"><path d="M1 1h11v7H5l-3 2.5V8H1z" fill="#555"/></svg></div>
  <div class="badge" style="left:191px;top:977px">6</div>
  <div class="icon-btn" style="left:213px;top:987px"><svg width="12" height="12" viewBox="0 0 12 12"><circle cx="9.5" cy="2.5" r="1.8" fill="#555"/><circle cx="2.5" cy="6" r="1.8" fill="#555"/><circle cx="9.5" cy="9.5" r="1.8" fill="#555"/><path d="M9.5 2.5 2.5 6l7 3.5" stroke="#555" fill="none"/></svg></div>
  <span class="read-more" style="left:698px;top:998px">&gt; Read More</span>

  <article class="post" style="top:1048px">
    <div class="post-img" role="img" aria-label="Photo of three smiling women in sunglasses on a city street"></div>
    <div class="post-band"><h2>SEMPER AT EGESTAS SED...</h2><div class="brand"><span class="dot"></span>Pelorn</div></div>
    <p class="post-meta">By <b>Dalen Morcroft</b> Business, <b>Education, Health</b> Posted <b>May 24, 2013</b></p>
    <p class="post-text body-copy">Suspendisse blandit ligula turpis, ac convallis risus fermentum non. Duis vestibulum quis quam vel accumsan. Nunc a vulputate lectus. Vestibulum eleifend nisl sed massa sagittis vestibulum. Vestibulum pretium blandit tellus, sodales volutpat sapien varius vel. Phasellus tristique cursus erat, a placerat tellus laoreet eget. Fusce vitae dui sit amet lacus rutrum convallis. Vivamus sit amet lectus venenatis est rhoncus interdum a vitae velit.</p>
    <div class="icon-btn" style="left:18px;top:442px"><svg width="13" height="11" viewBox="0 0 13 11"><path d="M1 1h11v7H5l-3 2.5V8H1z" fill="#555"/></svg></div>
    <div class="badge" style="left:37px;top:432px">6</div>
    <div class="icon-btn" style="left:59px;top:442px"><svg width="12" height="12" viewBox="0 0 12 12"><circle cx="9.5" cy="2.5" r="1.8" fill="#555"/><circle cx="2.5" cy="6" r="1.8" fill="#555"/><circle cx="9.5" cy="9.5" r="1.8" fill="#555"/><path d="M9.5 2.5 2.5 6l7 3.5" stroke="#555" fill="none"/></svg></div>
    <span class="read-more" style="left:509px;top:457px">&gt; Read More</span>
  </article>

  <article class="post" style="top:1564px">
    <div class="post-img" role="img" aria-label="Photo of three smiling women in sunglasses on a city street"></div>
    <div class="post-band"><h2>SEMPER AT EGESTAS SED...</h2><div class="brand"><span class="dot"></span>Pelorn</div></div>
    <p class="post-meta">By <b>Dalen Morcroft</b> Business, <b>Education, Health</b> Posted <b>May 24, 2013</b></p>
    <p class="post-text body-copy">Suspendisse blandit ligula turpis, ac convallis risus fermentum non. Duis vestibulum quis quam vel accumsan. Nunc a vulputate lectus. Vestibulum eleifend nisl sed massa sagittis vestibulum. Vestibulum pretium blandit tellus, sodales volutpat sapien varius vel. Phasellus tristique cursus erat, a placerat tellus laoreet eget. Fusce vitae dui sit amet lacus rutrum convallis. Vivamus sit amet lectus venenatis est rhoncus interdum a vitae velit.</p>
    <div class="icon-btn" style="left:18px;top:442px"><svg width="13" height="11" viewBox="0 0 13 11"><path d="M1 1h11v7H5l-3 2.5V8H1z" fill="#555"/></svg></div>
    <div class="badge" style="left:37px;top:432px">6</div>
    <div class="icon-btn" style="left:59px;top:442px"><svg width="12" height="12" viewBox="0 0 12 12"><circle cx="9.5" cy="2.5" r="1.8" fill="#555"/><circle cx="2.5" cy="6" r="1.8" fill="#555"/><circle cx="9.5" cy="9.5" r="1.8" fill="#555"/><path d="M9.5 2.5 2.5 6l7 3.5" stroke="#555" fill="none"/></svg></div>
    <span class="read-more" style="left:509px;top:457px">&gt; Read More</span>
  </article>

  <div class="abs load-more"><svg width="12" height="14" viewBox="0 0 12 14"><path d="M6 1v11M1.5 7.5 6 12l4.5-4.5" stroke="#777" stroke-width="1.6" fill="none"/></svg>LOAD MORE</div>
</main>

<aside>
  <p class="abs social-label">SOCIAL<br>MEDIA :</p>
  <div class="soc" style="left:853px;background:#3b5b9a"></div>
  <div class="soc" style="left:888px;background:#3fa7dd"></div>
  <div class="soc" style="left:923px;background:#d3322c"></div>
  <div class="soc" style="left:958px;background:#2aa7d6"></div>
  <div class="soc" style="left:994px;background:#e8672a"></div>

  <div class="ad ad1" role="img" aria-label="Banner photo of a joyful woman raising a glass">
    <p>Reclaim your power when you feel powerless.</p>
    <div class="brand"><span class="dot"></span>Pelorn</div>
  </div>
  <div class="ad ad2" role="img" aria-label="Banner photo of a smiling woman resting her chin on her hand in warm sunlight">
    <span class="ad-corner"></span>
    <div class="band"><p>Reclaim your power when you feel powerless.</p></div>
    <div class="brand">Pelorn</div>
  </div>
  <div class="ad ad3" role="img" aria-label="Banner photo of a glamorous woman with a black hat and pearls">
    <span class="ad-corner" style="left:16px;top:16px"></span>
    <p>Reclaim<br>your<br>power<br>when you<br>feel<br>powerless.</p>
  </div>

  <h3 class="abs side-label" style="left:788px;top:1204px">Popular Posts</h3>
  <div class="pop-item" style="top:1235px"><div class="pop-img" style="background:linear-gradient(90deg,#eee,#b9968a)" role="img" aria-label="Portrait photo of a woman"></div><p class="pop-title">Semper at egestas sed, elementum in justo</p><p class="pop-date" style="top:52px">May 24, 2013</p></div>
  <div class="pop-item" style="top:1329px"><div class="pop-img" style="background:linear-gradient(180deg,#cfd8dc,#9a8d74)" role="img" aria-label="Photo of a woman reading outdoors"></div><p class="pop-title">Semper at egestas sed, elementum in justo</p><p class="pop-date" style="top:52px">May 24, 2013</p></div>
  <div class="pop-item" style="top:1423px"><div class="pop-img" style="background:linear-gradient(90deg,#ece8ee,#c7b9c6)" role="img" aria-label="Photo of a joyful woman raising a glass"></div><p class="pop-title">Semper at egestas sed, elementum in justo</p><p class="pop-date" style="top:52px">May 24, 2013</p></div>
  <div class="pop-item" style="top:1517px"><div class="pop-img" style="background:linear-gradient(135deg,#111,#444 60%,#a11)" role="img" aria-label="Photo of a woman with a dramatic red and black look"></div><p class="pop-title">Semper at egestas sed, elementum in justo</p><p class="pop-date" style="top:52px">May 24, 2013</p></div>

  <h3 class="abs side-label" style="left:788px;top:1629px">Video</h3>
  <div class="abs video" role="img" aria-label="Video still of an outstretched hand on a golden background"></div>
  <svg class="abs" style="left:892px;top:1703px" width="30" height="30" viewBox="0 0 30 30"><circle cx="15" cy="15" r="12" fill="none" stroke="#2a1d06" stroke-width="2"/><path d="M12 9.5 20 15l-8 5.5z" fill="#2a1d06"/></svg>

  <h3 class="abs side-label" style="left:790px;top:1809px">Recent Comments</h3>
  <div class="comment" style="top:1843px"><svg width="10" height="9" viewBox="0 0 10 9"><path d="M0 0h10v6H4L1.5 8.5V6H0z" fill="#bbb"/></svg>Admin On Proin Et Dignissim Magna</div>
  <div class="comment" style="top:1870px"><svg width="10" height="9" viewBox="0 0 10 9"><path d="M0 0h10v6H4L1.5 8.5V6H0z" fill="#bbb"/></svg>Admin On Proin Et Dignissim Magna</div>
  <div class="comment" style="top:1897px"><svg width="10" height="9" viewBox="0 0 10 9"><path d="M0 0h10v6H4L1.5 8.5V6H0z" fill="#bbb"/></svg>Admin On Proin Et Dignissim Magna</div>
  <div class="comment" style="top:1925px"><svg width="10" height="9" viewBox="0 0 10 9"><path d="M0 0h10v6H4L1.5 8.5V6H0z" fill="#bbb"/></svg>Admin On Proin Et Dignissim Magna</div>
</aside>

<footer>
  <div class="abs site-footer"></div>
  <nav class="foot-nav">
    <span class="current" style="left:172px">Home</span>
    <span style="left:245px">About</span>
    <span style="left:324px">Work With Me</span>
    <span style="left:453px">Praise</span>
    <span style="left:535px">Giving Back</span>
    <span style="left:651px">Privacy Policy</span>
    <span style="left:785px">Sitemap</span>
  </nav>
  <div class="brand" style="position:absolute;left:926px;top:2130px;font-size:18px"><span class="dot" style="width:34px;height:34px"></span>Pelorn</div>
  <p class="abs foot-label" style="left:172px;top:2204px">Newsletter Subscription:</p>
  <div class="field foot-field" style="left:172px;top:2235px;width:183px;height:30px">First name</div>
  <div class="field foot-field" style="left:360px;top:2235px;width:183px;height:30px">Email</div>
  <div class="btn-sub" style="left:548px;top:2235px;width:86px;height:30px;background:#222;border:1px solid #444">SUBSCRIBE</div>
  <p class="abs foot-label" style="left:840px;top:2204px">Social Media:</p>
  <div class="foot-soc" style="left:840px"></div>
  <div class="foot-soc" style="left:875px"></div>
  <div class="foot-soc" style="left:911px;background:#c2312b"></div>
  <div class="foot-soc" style="left:946px"></div>
  <div class="foot-soc" style="left:982px"></div>
</footer>

</body>
</html>
```